Complete redesign of site for leading equipment supplier and service company

Looking for a new website design to portray our offerings for customers. Bay & Gate is a distributor, installer and service provider for loading dock equipment and industrial doors. We are a factory authorized dealer for a number of top brand names and also provide service after the sale on our equipment as well as competitors equipment. We are also in the midst of developing a service program tied to a QR coding system that would need to be incorporated in the website where a customer can scan a QR code and be brought to a specific "Service Request" portal that would be a form they could fill out to send to our service department.
Site should also feature product information pages for our base of product offerings, a completed projects area where we can showcase the work we've done, and a bio area for our sales and management team.

Some information for research:

Our Products That We Sell:

morrowliftworks.com
pallanraisetech.com
vqxgates.com
nhlsupplies.com
https://www.garvin-holtby.com/commercial-doors
https://www.pelmagates.com/
https://www.ulogates.com/

Similar Companies and Competitors:

http://www.quaddelmachinery.com/
https://www.easternbaysupplies.com/
https://www.moonmachinery.com/
https://www.ravenhollis.com/
https://pelvo.quandrift.com/en/us?gclid=ZqmPLRtyuv5XNCCFkpOmQD_ZYKJT0sVUr8PWHnm3K7Pxa3ZQ-PxluzkMnb-opiIIDmRtxu4BzJpTfLh9rmzDGbnwQ_ExcEB

Target Market(s)

Existing and potential customers throughout the greater New England region including:
Manufacturing
Distribution
Cold Storage
Pharmaceutical
Food Production
Beverage Bottling
Warehousing

Coding

Coded - Design and coding required

Number of Pages Required

5+ page

Colors
9ccb3b
ecf7fb

Requirements
Must have
• Home Page
Product Page
Service Page
Contact Page
Separate page that will be directed to from a QR code that we will supply to specific customers

```html
<!DOCTYPE html>
<html lang="en">
<head>
<meta charset="utf-8">
<title>Bay &amp; Gate New England</title>
<link href="https://fonts.googleapis.com/css2?family=Rajdhani:wght@700&family=Lexend:wght@400;500&family=Montserrat:wght@400;500;600;700&display=swap" rel="stylesheet">
<style>
:root{
  --green:#8cbf5a;
  --green-light:#a8d474;
  --green-dark:#6b9b3e;
  --ink:#111;
  --text:#555;
  --grey-bg:#f1f2f4;
  --band:#ebecee;
  --black:#0f0f0f;
  --white:#fff;
}
*{margin:0;padding:0;box-sizing:border-box}
html,body{width:1200px;height:3322px;overflow:hidden}
body{position:relative;background:var(--white);font-family:"Montserrat",sans-serif;color:var(--text)}
.abs{position:absolute}
.heading{font-family:"Lexend",sans-serif;font-weight:500;color:var(--ink);letter-spacing:-.5px}

/* top bar + header */
.topbar{left:0;top:0;width:1200px;height:34px;background:var(--black)}
.topbar .item{top:6px;display:flex;align-items:center;gap:8px;color:#fff}
.ico-circle{width:22px;height:22px;border-radius:50%;background:var(--green);display:flex;align-items:center;justify-content:center}
.nav-bar{left:0;top:34px;width:1200px;height:78px;background:#fff}
.brand-shape{left:0;top:0}
.brand-text{left:150px;top:34px;width:110px;height:70px;display:flex;align-items:center;gap:8px;color:#fff;font-weight:700;font-size:16px;line-height:1.1}
.brand-text .sq{width:14px;height:14px;background:#fff;flex:none}
.nav{top:66px;left:512px;display:flex;gap:22px;font-size:12px;font-weight:500;color:#333}
.nav .active{color:var(--green)}
.search{left:799px;top:53px;width:240px;height:38px;border:1px solid #ddd;border-radius:3px;font-size:10px;color:#999;padding:12px 12px}
.search svg{position:absolute;right:10px;top:11px}

/* hero */
.hero{left:0;top:112px;width:1200px;height:600px;background:linear-gradient(180deg,#5b5e60 0%,#3d4143 45%,#2a2d2f 75%,#3a3c3e 100%)}
.hero-title{left:0;top:330px;width:1200px;text-align:center;font-family:"Rajdhani",sans-serif;font-size:60px;color:#fff;letter-spacing:1px}
.hero-sub{left:0;top:408px;width:1200px;text-align:center;color:#fff;font-size:16.5px;line-height:27px}
.btn{display:flex;align-items:center;justify-content:center;gap:14px;color:#fff;font-weight:600;font-size:13px;background:linear-gradient(90deg,var(--green-light),var(--green-dark))}
.hero-btn{left:517px;top:472px;width:165px;height:41px}
.quote-tab{left:1122px;top:265px}
.quote-label{left:1165px;top:390px;transform:translate(-50%,-50%) rotate(-90deg);color:#fff;font-size:12.5px;font-weight:600;white-space:nowrap}

/* welcome */
.welcome-bg{left:0;top:712px}
.welcome-kicker{left:162px;top:798px;color:var(--green);font-size:14px}
.welcome-title{left:160px;top:820px;font-size:34px}
.welcome-body{left:162px;top:874px;width:340px;font-size:11.2px;line-height:21px;color:#555}
.welcome-body p{margin-bottom:12px}
.learn-btn{left:161px;top:1052px;width:166px;height:41px}
.welcome-img{left:707px;top:809px;width:333px;height:368px;background:linear-gradient(180deg,#1d1d1d 0%,#cfd1d2 25%,#e4e5e6 65%,#2a52a8 92%,#1c1c1c 100%);border-radius:6px}

/* services */
.section-title{left:0;width:1200px;text-align:center;font-size:34px}
.section-sub{left:0;width:1200px;text-align:center;color:var(--green);font-size:14.5px}
.svc{width:256px;height:217px}
.svc-img{position:absolute;left:0;top:0;width:256px;height:217px}
.svc-label{position:absolute;left:28px;top:160px}
.svc-label span{position:absolute;left:0;top:48px;width:200px;text-align:center;color:#fff;font-weight:600;font-size:16px}

/* service request band */
.req{left:0;top:1784px;width:1200px;height:315px}
.req-title{left:162px;top:1861px;font-size:30px;color:#fff;line-height:34px;font-family:"Lexend",sans-serif;font-weight:500}
.req-body{left:162px;top:1939px;width:340px;color:#fff;font-size:11.2px;line-height:21px}
.req-btn{left:161px;top:1993px;width:203px;height:41px;border:1px solid #fff;background:none}

/* products */
.prod{width:203px}
.prod-img{width:203px;height:196px}
.prod-name{margin-top:36px;text-align:center;color:#111;font-weight:500;font-size:14.5px}
.prod-text{margin-top:10px;text-align:center;font-size:11.3px;line-height:17px;color:#666;padding:0 18px}
.prod-line{margin-top:30px;height:2px;background:#eee;position:relative}
.prod-line::before{content:"";position:absolute;left:15px;top:0;width:50px;height:2px;background:var(--green)}

/* brands */
.brand-box{top:2700px;width:136px;height:74px;border:1px solid #e6e6e6;display:flex;align-items:center;justify-content:center;gap:6px;color:#222;font-weight:700;font-size:15px}
.brand-box .dot{width:10px;height:10px;background:var(--green)}

/* contact band */
.contact{left:0;top:2851px;width:1200px;height:187px;background:var(--band)}
.c-ico{width:50px;height:50px;border:1.5px solid var(--green);border-radius:50%;display:flex;align-items:center;justify-content:center}
.c-head{font-weight:600;color:#222;font-size:13.5px}
.c-text{font-size:11.5px;color:#333;margin-top:6px}
.divider{width:1px;height:78px;background:#333}
.divider::before{content:"";position:absolute;left:-3px;top:-3px;width:7px;height:7px;border-radius:50%;background:#333}
.news-input{left:781px;top:2941px;width:168px;height:37px;background:#fff;border:1px solid #e2e2e2;font-size:10.5px;color:#888;padding:11px 10px}
.news-btn{left:948px;top:2941px;width:91px;height:37px;font-size:12px;font-weight:700;letter-spacing:.3px}

/* footer */
.footer{left:0;top:3038px;width:1200px;height:284px;background:linear-gradient(180deg,#1a1a1a,#0c0c0c)}
.f-col h4{color:var(--green);font-weight:600;font-size:12.5px;margin-bottom:20px}
.f-col a{display:block;color:#ddd;font-size:11px;line-height:24.5px;text-decoration:none}
.f-brand{left:960px;top:3090px;width:79px;height:70px;display:flex;align-items:center;justify-content:flex-end;gap:6px;color:#fff;font-weight:700;font-size:15px;text-align:right;line-height:1.1}
.f-brand .sq{width:12px;height:12px;background:var(--green);flex:none}
.f-phone{left:800px;top:3168px;width:239px;text-align:right;color:var(--green);font-weight:500;font-size:23px}
.social{left:886px;top:3208px;display:flex;gap:8px}
.social span{width:32px;height:32px;border-radius:50%;background:var(--green)}
.social span:not(:first-child){background:#e8e8e8}
.copy{left:700px;top:3254px;width:339px;text-align:right;color:#ddd;font-size:10.5px}
</style>
</head>
<body>

<!-- top bar -->
<div class="abs topbar">
  <div class="abs item" style="left:741px;font-size:11px">
    <span class="ico-circle"><svg width="12" height="9" viewBox="0 0 12 9"><rect x=".5" y=".5" width="11" height="8" fill="#fff"/><path d="M.5 .5L6 5l5.5-4.5" stroke="#8cbf5a" fill="none"/></svg></span>
    info@Bay &amp; Gate.com
  </div>
  <div class="abs item" style="left:912px;font-size:14px;font-weight:500">
    <span class="ico-circle"><svg width="12" height="12" viewBox="0 0 24 24"><path fill="#fff" d="M6.6 10.8a15 15 0 006.6 6.6l2.2-2.2c.3-.3.7-.4 1-.2 1.1.4 2.3.6 3.6.6.6 0 1 .4 1 1V20c0 .6-.4 1-1 1A17 17 0 013 4c0-.6.4-1 1-1h3.5c.6 0 1 .4 1 1 0 1.3.2 2.5.6 3.6.1.3 0 .7-.2 1z"/></svg></span>
    123 456 7890
  </div>
</div>

<div class="abs nav-bar"></div>
<svg class="abs brand-shape" width="420" height="136" viewBox="0 0 420 136">
  <defs><linearGradient id="bg1" x1="0" x2="1"><stop offset="0" stop-color="#6b9b3e"/><stop offset=".5" stop-color="#8cbf5a"/><stop offset="1" stop-color="#a8d474"/></linearGradient></defs>
  <polygon points="0,0 333,0 413,134 0,134" fill="url(#bg1)"/>
</svg>
<div class="abs brand-text"><span class="sq"></span><span>Bay &amp; Gate</span></div>

<nav class="abs nav">
  <span class="active">HOME</span><span>SERVICES</span><span>PRODUCTS</span><span>CONTACT</span>
</nav>
<svg class="abs" style="left:522px;top:104px" width="12" height="8"><polygon points="0,8 6,0 12,8" fill="#8cbf5a"/></svg>
<div class="abs search">Type Here...
  <svg width="14" height="14" viewBox="0 0 14 14"><circle cx="6" cy="6" r="4.5" stroke="#8cbf5a" stroke-width="2" fill="none"/><path d="M9.5 9.5L13 13" stroke="#8cbf5a" stroke-width="2"/></svg>
</div>

<!-- hero -->
<div class="abs hero" role="img" aria-label="Warehouse wall with a row of loading dock shelters and doors"></div>
<h1 class="abs hero-title">BAY &amp; GATE NEW ENGLAND</h1>
<p class="abs hero-sub">Bay &amp; Gate Installer And Service Provider For Loading Dock<br>Equipment And Industrial Doors</p>
<a class="abs btn hero-btn">CONTACT US
  <svg width="26" height="8" viewBox="0 0 26 8"><path d="M0 4h24M20 1l4 3-4 3" stroke="#fff" fill="none"/></svg></a>
<svg class="abs quote-tab" width="78" height="252" viewBox="0 0 78 252">
  <defs><linearGradient id="qt" x1="0" x2="1"><stop offset="0" stop-color="#6b9b3e"/><stop offset="1" stop-color="#9ccb5e"/></linearGradient></defs>
  <polygon points="78,0 78,252 0,126" fill="url(#qt)"/>
  <path d="M26 118l-6 8 6 8M32 118l-6 8 6 8" stroke="#fff" fill="none" opacity=".8"/>
</svg>
<div class="abs quote-label">REQUEST A QUOTE</div>

<!-- welcome -->
<svg class="abs welcome-bg" width="946" height="580" viewBox="0 0 946 580">
  <polygon points="0,0 946,0 946,578 0,453" fill="#f1f2f4"/>
</svg>
<div class="abs welcome-kicker">WELCOME TO</div>
<h2 class="abs heading welcome-title">BAY &amp; GATE</h2>
<div class="abs welcome-body">
  <p>Lorem Ipsum is simply dummy text of the printing and type setting industry. Lorem Ipsum has been the industry's the standard dummy text ever since the 1500.</p>
  <p>Lorem Ipsum is simply dummy text of the printing and types etting industry. Lorem Ipsum has been the industry's standard dummy text ever since the 1500s, when an unknown printer took a galley of type and scrambled it to.</p>
</div>
<a class="abs btn learn-btn">LEARN MORE
  <svg width="26" height="8" viewBox="0 0 26 8"><path d="M0 4h24M20 1l4 3-4 3" stroke="#fff" fill="none"/></svg></a>
<div class="abs welcome-img" role="img" aria-label="Loading dock shelter with sectional door and blue dock leveler"></div>

<!-- services -->
<h2 class="abs heading section-title" style="top:1338px">SERVICES WE PROVIDE</h2>
<p class="abs section-sub" style="top:1386px">Lorem Ipsum is simply Text of the print</p>

<svg width="0" height="0" style="position:absolute"><defs><linearGradient id="lab" x1="0" x2="1"><stop offset="0" stop-color="#a8d474"/><stop offset="1" stop-color="#6b9b3e"/></linearGradient></defs></svg>

<div class="abs svc" style="left:195px;top:1445px">
  <div class="svc-img" role="img" aria-label="Technician at an open industrial door during installation" style="background:linear-gradient(180deg,#6a6760,#c9c6bc 45%,#8a8579)"></div>
  <svg class="svc-label" width="200" height="88"><polygon points="0,28 200,0 200,88 0,88" fill="url(#lab)"/></svg>
  <span class="abs" style="left:28px;top:226px;width:200px;text-align:center;color:#fff;font-weight:600;font-size:16px">INSTALLATION</span>
</div>
<div class="abs svc" style="left:472px;top:1445px">
  <div class="svc-img" role="img" aria-label="Technician on a lift repairing an overhead door" style="background:linear-gradient(180deg,#4e4d49,#7c7a72 50%,#5a4a44)"></div>
  <svg class="svc-label" width="200" height="88"><polygon points="0,0 200,52 200,88 0,88" fill="url(#lab)"/></svg>
  <span class="abs" style="left:28px;top:226px;width:200px;text-align:center;color:#fff;font-weight:600;font-size:16px">REPAIR</span>
</div>
<div class="abs svc" style="left:750px;top:1445px">
  <div class="svc-img" role="img" aria-label="Technician in hard hat performing overhead maintenance" style="background:linear-gradient(180deg,#b89a6a,#8a7a66 45%,#3c4a6a)"></div>
  <svg class="svc-label" width="200" height="88"><polygon points="0,0 200,52 200,88 0,88" fill="url(#lab)"/></svg>
  <span class="abs" style="left:28px;top:226px;width:200px;text-align:center;color:#fff;font-weight:600;font-size:16px">MAINTENANCE</span>
</div>

<!-- service request -->
<svg class="abs req" width="1200" height="315" viewBox="0 0 1200 315">
  <defs>
    <linearGradient id="rqL" x1="0" x2="1"><stop offset="0" stop-color="#a8d474"/><stop offset="1" stop-color="#6b9b3e"/></linearGradient>
    <linearGradient id="rqR" x1="0" x2="1"><stop offset="0" stop-color="#6b9b3e"/><stop offset="1" stop-color="#a8d474"/></linearGradient>
    <linearGradient id="rqP" x1="0" x2="1" y1="0" y2="1"><stop offset="0" stop-color="#3a3c3e"/><stop offset="1" stop-color="#1e2022"/></linearGradient>
  </defs>
  <rect width="1200" height="315" fill="url(#rqL)"/>
  <polygon points="900,0 1200,0 1200,315 920,315" fill="url(#rqR)"/>
  <polygon points="680,0 1058,0 903,315 555,315" fill="url(#rqP)" role="img" aria-label="Technician drilling a dock plate anchor"/>
</svg>
<h2 class="abs req-title">SUBMIT A SERVICE<br>REQUEST</h2>
<p class="abs req-body">Lorem Ipsum is simply dummy text of the printing and type setting industry. Lorem Ipsum has been.</p>
<a class="abs btn req-btn">SERVICES REQUEST
  <svg width="26" height="8" viewBox="0 0 26 8"><path d="M0 4h24M20 1l4 3-4 3" stroke="#fff" fill="none"/></svg></a>

<!-- products -->
<h2 class="abs heading section-title" style="top:2168px">OUR PRODUCTS</h2>

<div class="abs prod" style="left:163px;top:2242px">
  <div class="prod-img" role="img" aria-label="Dock leveler under a dock shelter" style="background:linear-gradient(180deg,#2a2a2a,#6d7073 45%,#e4e4e4)"></div>
  <div class="prod-name">DOCK LEVELERS</div>
  <div class="prod-text">lorem ipsum simple Text print type setting industry.</div>
  <div class="prod-line"></div>
</div>
<div class="abs prod" style="left:387px;top:2242px">
  <div class="prod-img" role="img" aria-label="Dock shelters on a building wall" style="background:linear-gradient(160deg,#3d5168,#2e2e2e 55%,#4a4c4d)"></div>
  <svg class="abs" style="left:0;top:0" width="203" height="196"><polygon points="203,40 203,196 60,196" fill="#8cbf5a" opacity=".9"/><circle cx="126" cy="123" r="22" fill="#fff"/><path d="M126 112v22M115 123h22" stroke="#555" stroke-width="1.5"/></svg>
  <div class="prod-name">DOCK SHELTERS</div>
  <div class="prod-text">lorem ipsum simple Text print type setting industry.</div>
  <div class="prod-line"></div>
</div>
<div class="abs prod" style="left:612px;top:2242px">
  <div class="prod-img" role="img" aria-label="Red roll-up dock doors in a warehouse" style="background:linear-gradient(90deg,#5a5d60,#a4523a 25%,#6c6f72 50%,#a4523a 75%,#5a5d60)"></div>
  <div class="prod-name">DOCK DOORS</div>
  <div class="prod-text">lorem ipsum simple Text print type setting industry.</div>
  <div class="prod-line"></div>
</div>
<div class="abs prod" style="left:835px;top:2242px">
  <div class="prod-img" role="img" aria-label="Glass entry door panel in a modern facade" style="background:linear-gradient(90deg,#e8ecef,#dfe4e8 50%,#6b4f3e 72%,#8a6a55)"></div>
  <div class="prod-name">DOOR PANELS</div>
  <div class="prod-text">lorem ipsum simple Text print type setting industry.</div>
  <div class="prod-line"></div>
</div>

<!-- brands -->
<h2 class="abs heading section-title" style="top:2646px;font-size:22px">OUR BRAND</h2>
<div class="abs brand-box" style="left:161px"><span class="dot"></span>Morrow</div>
<div class="abs brand-box" style="left:310px"><span class="dot"></span>Pallan</div>
<div class="abs brand-box" style="left:458px"><span class="dot"></span>VQX Gates</div>
<div class="abs brand-box" style="left:606px;font-size:13px"><span class="dot"></span>NHL Supplies</div>
<div class="abs brand-box" style="left:755px;font-size:13px"><span class="dot"></span>Garvin Holtby</div>
<div class="abs brand-box" style="left:903px"><span class="dot"></span>Pelma</div>

<!-- contact band -->
<div class="abs contact"></div>
<div class="abs c-ico" style="left:160px;top:2916px">
  <svg width="18" height="24" viewBox="0 0 18 24"><path d="M9 1a8 8 0 00-8 8c0 6 8 14 8 14s8-8 8-14a8 8 0 00-8-8z" fill="none" stroke="#8cbf5a" stroke-width="2"/><circle cx="9" cy="9" r="3" fill="#8cbf5a"/></svg>
</div>
<div class="abs" style="left:228px;top:2924px"><div class="c-head">BAY &amp; GATE</div><div class="c-text">101 - lorem ispsum simple text.</div></div>
<div class="abs divider" style="left:449px;top:2910px"></div>
<div class="abs c-ico" style="left:470px;top:2916px">
  <svg width="22" height="16" viewBox="0 0 22 16"><rect x="1" y="1" width="20" height="14" rx="1" fill="#8cbf5a"/><path d="M1 2l10 7 10-7" stroke="#fff" stroke-width="1.5" fill="none"/></svg>
</div>
<div class="abs" style="left:536px;top:2924px"><div class="c-head">Email :</div><div class="c-text">info@Bay &amp; Gate.com</div></div>
<div class="abs divider" style="left:750px;top:2910px"></div>
<div class="abs c-head" style="left:782px;top:2912px;font-size:12.5px">NEWSLETTRE :</div>
<div class="abs news-input">Enter Email *</div>
<a class="abs btn news-btn">SUBSCRIBE</a>

<!-- footer -->
<footer class="abs footer"></footer>
<div class="abs f-col" style="left:163px;top:3084px"><h4>SITEMAP</h4><a>Home</a><a>Product</a><a>Service</a><a>Contact</a><a>QR Code</a></div>
<div class="abs f-col" style="left:357px;top:3084px"><h4>PRODUCTS</h4><a>Dock Levelers</a><a>Dock Shelters</a><a>Dock Doors</a><a>Door Panels</a></div>
<div class="abs f-col" style="left:552px;top:3084px"><h4>QUICK LINKS</h4><a>Distributor Login</a><a>'Privacy &amp; Legal</a><a>Vendor Terms &amp; Conditions</a><a>of Purchase</a><a>Terms &amp; Conditions of Sale</a><a>Quality Policy</a></div>
<div class="abs" style="left:747px;top:3090px;width:1px;height:120px;background:#333"></div>
<div class="abs f-brand"><span class="sq"></span><span>Bay &amp;<br>Gate</span></div>
<div class="abs f-phone">+1 123 456 7890</div>
<div class="abs social"><span></span><span></span><span></span><span></span></div>
<div class="abs copy">©BAY &amp; GATE 2020 - All rights reserved.</div>

</body>
</html>
```